Club Lumora - Dermatology Consultation App

Club Lumora is launching a new Quince QWS App for online Dermatology consultation. We would appreciate a simple Scandinavian design which communicates trust, comfort and expensive feel. Most yacht designs have similar color palette, light wood colors and textures, but don’t be restricted by those in your artistic search.
The process is completed in three easy steps:
1. take a Snapshot.
2. Describe and Send it.
3. get Diagnosis and Treatment.
The Home screen should also have buttons - Start new Case, Follow up Visit, Rx Refill.
15% of the Home screen should also have a field/button - Medical Cosmetics Shop.
10% of the Home screen should also have a field or buttons for Our Partners (sponsors) – Talvine, Norelisa, Parlo, Ostra. (if you click you would be directed to their sites)
Note / Suggestion : Maybe you could use a larger picture of a dermatologist and have overlying fields and content, just for more influencing effect. (I am not a professional though)
Thank you so much.
Updates
Target Market(s)
24 - 59 Female
Industry/Entity Type
Club
Look and feel

```html
<!DOCTYPE html>
<html lang="en">
<head>
<meta charset="utf-8">
<title>Club Lumora – Start Screen</title>
<link href="https://fonts.googleapis.com/css2?family=Montserrat:wght@400;500&display=swap" rel="stylesheet">
<style>
  :root {
    --canvas-bg: #b4bdc3;
    --screen-bg: #f4f3f5;
    --bar-bg: #ffffff;
    --ink: #2b2b2f;
    --plum-text: #5b4552;
    --row-bg: #ffffff;
    --row-line: #e3e1e5;
    --shop-bg: #e2dfe4;
    --partner-bg: #4d2b3d;
    --partner-ink: #ffffff;
    --dot: rgba(255,255,255,0.45);
    --dot-active: #ffffff;
  }
  * { box-sizing: border-box; margin: 0; padding: 0; }
  html, body { width: 1200px; height: 1100px; overflow: hidden; }
  body {
    background: var(--canvas-bg);
    font-family: "Montserrat", sans-serif;
    color: var(--ink);
    display: flex;
    align-items: center;
    justify-content: center;
  }
  .phone-screen {
    width: 583px;
    height: 1040px;
    background: var(--screen-bg);
    display: flex;
    flex-direction: column;
  }
  .status-bar {
    height: 44px;
    background: var(--bar-bg);
    display: flex;
    align-items: center;
    justify-content: space-between;
    padding: 0 14px;
    font-size: 20px;
    font-weight: 500;
  }
  .status-left, .status-right { display: flex; align-items: center; gap: 6px; width: 170px; }
  .status-right { justify-content: flex-end; }
  .signal { letter-spacing: -2px; font-size: 15px; }
  .nav-bar {
    height: 77px;
    background: var(--bar-bg);
    display: grid;
    grid-template-columns: 1fr auto 1fr;
    align-items: center;
    padding: 0 18px;
    font-size: 21px;
    letter-spacing: 0.5px;
    border-bottom: 4px solid #e8e7ea;
  }
  .nav-back { display: flex; align-items: center; gap: 10px; }
  .nav-title { font-weight: 500; }
  .nav-search { justify-self: end; }
  .hero {
    position: relative;
    height: 402px;
    margin: 0 6px;
  }
  .hero-photo {
    position: absolute; inset: 0;
    background: linear-gradient(90deg, #dfe4e4 0%, #cfb7ab 22%, #c2927e 48%, #9c7668 70%, #4f4548 86%, #d9dadf 100%);
  }
  .brand {
    position: absolute;
    left: 16px; top: 88px;
    width: 240px;
    text-align: center;
  }
  .brand-mark {
    display: flex; align-items: center; justify-content: center; gap: 12px;
    font-size: 33px; color: #3a2a33; font-weight: 400;
  }
  .brand-circle {
    width: 84px; height: 84px; border-radius: 50%;
    border: 2px solid #3a2a33;
  }
  .brand-tagline {
    margin-top: 14px;
    font-size: 17px; line-height: 1.25; color: #3a2a33; letter-spacing: 0.5px;
  }
  .pager {
    position: absolute; bottom: 16px; left: 215px;
    display: flex; gap: 15px;
  }
  .pager span { width: 14px; height: 14px; border-radius: 50%; background: var(--dot); }
  .pager .is-active { background: var(--dot-active); }
  .menu { margin: 0 6px; }
  .menu-row {
    height: 86px;
    background: var(--row-bg);
    border-bottom: 2px solid var(--row-line);
    display: flex; align-items: center; justify-content: space-between;
    padding: 0 26px;
    font-size: 31px;
    color: var(--plum-text);
    letter-spacing: -0.3px;
  }
  .shop {
    margin: 0 6px;
    height: 132px;
    background: var(--shop-bg);
    display: flex; align-items: center; justify-content: center;
    font-size: 36px; color: var(--plum-text); letter-spacing: 0.5px;
  }
  .partners {
    margin: 0 6px;
    height: 86px;
    background: var(--partner-bg);
    display: flex; align-items: center; justify-content: space-evenly;
    color: var(--partner-ink);
    font-size: 26px; font-weight: 500;
  }
</style>
</head>
<body>
  <main class="phone-screen">
    <div class="status-bar">
      <div class="status-left"><span class="signal">●●●●●</span><span>Vantel</span>
        <svg width="20" height="16" viewBox="0 0 20 16"><path d="M1 5a13 13 0 0 1 18 0M4 8.5a8.5 8.5 0 0 1 12 0M7 12a4 4 0 0 1 6 0" fill="none" stroke="#2b2b2f" stroke-width="2"/><circle cx="10" cy="14.5" r="1.5" fill="#2b2b2f"/></svg>
      </div>
      <div class="status-time">9:23 AM</div>
      <div class="status-right">
        <svg width="16" height="16" viewBox="0 0 16 16"><path d="M15 1 1 7l7 1 1 7z" fill="#2b2b2f"/></svg>
        <span>66%</span>
        <svg width="42" height="18" viewBox="0 0 42 18"><rect x="1" y="1" width="36" height="16" rx="3" fill="none" stroke="#2b2b2f" stroke-width="1.5"/><rect x="3" y="3" width="22" height="12" rx="1.5" fill="#2b2b2f"/><rect x="38.5" y="6" width="2.5" height="6" fill="#2b2b2f"/></svg>
      </div>
    </div>

    <nav class="nav-bar">
      <div class="nav-back">
        <svg width="12" height="18" viewBox="0 0 12 18"><path d="M10 2 3 9l7 7" fill="none" stroke="#2b2b2f" stroke-width="2.5"/></svg>
        <span>BACK</span>
      </div>
      <div class="nav-title">START SCREEN</div>
      <svg class="nav-search" width="28" height="28" viewBox="0 0 28 28"><circle cx="12" cy="12" r="9.5" fill="none" stroke="#2b2b2f" stroke-width="2.2"/><path d="M19 19l7 7" stroke="#2b2b2f" stroke-width="2.4"/></svg>
    </nav>

    <section class="hero">
      <div class="hero-photo" role="img" aria-label="Dermatologist examining a mole on a patient's shoulder with a dermatoscope"></div>
      <div class="brand">
        <div class="brand-mark"><span class="brand-circle"></span><span>Club Lumora</span></div>
        <p class="brand-tagline">ONLINE DERMATOLOGY<br>CONSULTATION</p>
      </div>
      <div class="pager"><span></span><span></span><span></span><span class="is-active"></span><span></span></div>
    </section>

    <div class="menu">
      <div class="menu-row">START NEW CASE</div>
      <div class="menu-row">FOLLOW UP VISIT</div>
      <div class="menu-row">RX REFILL
        <svg width="14" height="24" viewBox="0 0 14 24"><path d="M3 3l9 9-9 9" fill="none" stroke="#2b2b2f" stroke-width="2.5"/></svg>
      </div>
    </div>

    <div class="shop">MEDICAL COSMETICS SHOP</div>

    <div class="partners">
      <span>Ostra</span><span>Parlo</span><span>Talvine</span><span>Norelisa</span>
    </div>
  </main>
</body>
</html>
```